High Design Value Gift Webstore Needs a Logo Design & Business Card Design

Design wanted: Logo and Business Card Design for an online store selling designer gifts (substantially Scandinavian design products). Business Card to feature Logo and company details on the front and the back to include discount/promotional code.

Site name: Gift Picks in Minutes

Site purpose: Enable time poor people to quickly select high design value gifts for special occasions (weddings, anniversaries, housewarmings, corporate gifts etc)

Products: A small selection of carefully selected high design value products ranging in price and across three categories: Display, Functional, Fun

Site design: We will be using a modern minimal Shopify theme and will also have a mobile site and an app. Our website is primarily black/white/grayscale - similar to this style: http://templates.vendorapla.com/templates/clean/styles/apparel

Target Market(s)

Customers with limited time who can quickly choose a gift from our pre selected range of 24 products.

Industry/Entity Type

Store

Logo Text

Gift Picks In Minutes

Requirements
Must have
• Modern design with company name included in the design, design needs to be modern and work well with our website - sample website (http://templates.vendorapla.com/templates/clean/styles/apparel).

```html
<!DOCTYPE html>
<html lang="en">
<head>
<meta charset="utf-8">
<title>Gift Picks in Minutes – Business Card</title>
<link rel="stylesheet" href="https://fonts.googleapis.com/css2?family=Quicksand:wght@500&family=Arimo:wght@400;700&display=swap">
<style>
  :root {
    --backdrop: #c9c9c9;
    --card-white: #ffffff;
    --card-black: #0b0b0b;
    --card-black-soft: #2a2a2a;
    --ink-dark: #1a1a1a;
    --silver-light: #f2f2f2;
    --silver-mid: #9a9a9a;
    --silver-dark: #5e5e5e;
    --name-grey: #8a8a8a;
    --contact-white: #f5f5f5;
  }
  * { margin: 0; padding: 0; box-sizing: border-box; }
  html, body {
    width: 1200px;
    height: 900px;
    overflow: hidden;
    background: var(--backdrop);
  }
  .canvas {
    position: relative;
    width: 1200px;
    height: 900px;
  }
  .business-card {
    position: absolute;
    left: 140px;
    top: 170px;
    width: 920px;
    height: 560px;
    border-radius: 42px;
    overflow: hidden;
    background: var(--card-white);
    box-shadow: 0 18px 40px rgba(0, 0, 0, 0.25);
  }
  .brand-area {
    position: absolute;
    inset: 0 0 auto 0;
    height: 310px;
    display: flex;
    align-items: center;
    justify-content: center;
    gap: 18px;
    padding-top: 40px;
  }
  .brand-square {
    width: 30px;
    height: 30px;
    background: var(--ink-dark);
  }
  .brand-name {
    font-family: "Quicksand", sans-serif;
    font-weight: 500;
    font-size: 46px;
    letter-spacing: 1px;
    color: var(--ink-dark);
  }
  .silver-band {
    position: absolute;
    left: 0;
    right: 0;
    top: 310px;
    height: 16px;
    background: linear-gradient(90deg, var(--silver-dark), var(--silver-light) 50%, var(--silver-mid));
  }
  .contact-area {
    position: absolute;
    left: 0;
    right: 0;
    top: 326px;
    bottom: 0;
    background: linear-gradient(180deg, var(--card-black-soft), var(--card-black) 45%);
    text-align: center;
    font-family: "Arimo", sans-serif;
    color: var(--contact-white);
  }
  .contact-name {
    margin-top: 26px;
    font-weight: 700;
    font-size: 32px;
    color: var(--name-grey);
  }
  .contact-phone {
    margin-top: 28px;
    font-size: 28px;
    letter-spacing: 1px;
  }
  .contact-email,
  .contact-web {
    font-size: 27px;
    margin-top: 8px;
  }
</style>
</head>
<body>
  <main class="canvas">
    <section class="business-card" aria-label="Gift Picks in Minutes business card">
      <header class="brand-area">
        <span class="brand-square" aria-hidden="true"></span>
        <h1 class="brand-name">Gift Picks in Minutes</h1>
      </header>
      <div class="silver-band" aria-hidden="true"></div>
      <div class="contact-area">
        <p class="contact-name">Mara Lindqvist</p>
        <p class="contact-phone">07700900418</p>
        <p class="contact-email">info@giftpicksinminutes.com</p>
        <p class="contact-web">www.giftpicksinminutes.com</p>
      </div>
    </section>
  </main>
</body>
</html>
```